Course Graduation Certificate

This project is not for a flyer but instead for the creation of a course graduation certificate. The final certificate needs to include the Marlowe Summit Aviation Academy logo and the text stating as follows:
Certifies that ___________________________ has satisfactorily completed the course of _______________________________ on ________________________________
I would also like to include some type of gold seal of completion as well as a place to sign my name and credentials at the bottom of the certificate
I have included the Marlowe Summit Aviation Academy logo as well as three other certificate examples for you to work from.
Target Market(s)
Students completing a certification course and receiving a certificate
Look and feel

```html
<!DOCTYPE html>
<html lang="en">
<head>
<meta charset="utf-8">
<title>Certificate of Completion – Marlowe Summit Aviation Academy</title>
<link rel="stylesheet" href="https://fonts.googleapis.com/css2?family=Cinzel:wght@700;900&family=Libre+Baskerville:ital,wght@1,400;1,700&family=Roboto:wght@400;700&display=swap">
<style>
  :root {
    --page-bg: #eceeee;
    --paper: #ffffff;
    --paper-line: #eef0f2;
    --ink: #2a2a2a;
    --ink-soft: #555a60;
    --brand-blue: #1d5fb0;
    --border-blue: #2f6fc0;
    --border-dark: #2b2b2b;
    --gold-light: #f4d27a;
    --gold-dark: #b8871f;
    --rule: #8a8f95;
    --watermark: #eef0f3;
  }
  html, body {
    margin: 0;
    width: 1200px;
    height: 800px;
    overflow: hidden;
    background: var(--page-bg);
  }
  .certificate {
    position: absolute;
    left: 0;
    top: 0;
    width: 1200px;
    height: 800px;
    background:
      repeating-linear-gradient(180deg, var(--paper) 0 5px, var(--paper-line) 5px 6px);
  }
  .certificate svg { display: block; }
  .title { font-family: "Cinzel", serif; font-weight: 900; fill: var(--ink); }
  .subtitle { font-family: "Cinzel", serif; font-weight: 700; fill: var(--ink); letter-spacing: 6px; }
  .script { font-family: "Libre Baskerville", serif; font-style: italic; font-weight: 700; fill: var(--brand-blue); }
  .filled { font-family: "Roboto", sans-serif; font-weight: 400; fill: var(--ink); }
  .label { font-family: "Libre Baskerville", serif; font-style: italic; font-weight: 700; fill: var(--ink-soft); }
  .brand-name { font-family: "Roboto", sans-serif; font-weight: 700; fill: var(--brand-blue); }
  .rule { stroke: var(--rule); stroke-width: 1.2; }
</style>
</head>
<body>
<main class="certificate">
  <svg width="1200" height="800" viewBox="0 0 1200 800" xmlns="http://www.w3.org/2000/svg">
    <defs>
      <radialGradient id="seal-gold" cx="40%" cy="35%" r="70%">
        <stop offset="0" stop-color="var(--gold-light)"/>
        <stop offset="1" stop-color="var(--gold-dark)"/>
      </radialGradient>
      <path id="title-arc" d="M 215 360 Q 600 40 985 360"/>
      <path id="subtitle-arc" d="M 395 352 Q 600 210 805 352"/>
    </defs>

    <!-- decorative border band -->
    <g class="border-band" role="img" aria-label="Decorative chevron border pattern">
      <rect x="28" y="28" width="1144" height="744" fill="none" stroke="var(--border-blue)" stroke-width="20" opacity="0.85"/>
      <rect x="18" y="18" width="20" height="764" fill="var(--border-dark)" opacity="0.85"/>
    </g>

    <!-- faint aircraft watermark area -->
    <ellipse class="watermark" role="img" aria-label="Faint aircraft silhouette watermark" cx="600" cy="520" rx="330" ry="120" fill="var(--watermark)"/>

    <!-- completion seal -->
    <g class="seal" role="img" aria-label="Gold seal of completion">
      <circle cx="1035" cy="130" r="72" fill="url(#seal-gold)"/>
      <circle cx="1035" cy="130" r="54" fill="var(--brand-blue)"/>
    </g>

    <text class="title" font-size="104" text-anchor="middle"><textPath href="#title-arc" startOffset="50%">CERTIFICATE</textPath></text>
    <text class="subtitle" font-size="28" text-anchor="middle"><textPath href="#subtitle-arc" startOffset="50%">★ OF COMPLETION ★</textPath></text>

    <text class="script" x="600" y="398" font-size="28" text-anchor="middle">Certifies that</text>
    <text class="filled" x="600" y="452" font-size="50" text-anchor="middle">Jordan Hale</text>
    <line class="rule" x1="250" y1="468" x2="950" y2="468"/>

    <text class="script" x="600" y="512" font-size="28" text-anchor="middle">has satisfactorily completed the course of</text>
    <text class="filled" x="600" y="566" font-size="34" text-anchor="middle">Stratus 450, 135 INHC</text>
    <line class="rule" x1="250" y1="580" x2="950" y2="580"/>

    <text class="script" x="405" y="640" font-size="28">on</text>
    <text class="filled" x="600" y="628" font-size="32" text-anchor="middle">25 August, 2025</text>
    <line class="rule" x1="450" y1="642" x2="760" y2="642"/>

    <g class="brand">
      <rect x="402" y="693" width="16" height="16" fill="var(--brand-blue)"/>
      <text class="brand-name" x="428" y="709" font-size="22">Marlowe Summit Aviation Academy</text>
    </g>

    <line class="rule" x1="840" y1="668" x2="1100" y2="668"/>
    <text class="label" x="970" y="694" font-size="18" text-anchor="middle">Authorized Signatory</text>

    <line class="rule" x1="100" y1="722" x2="360" y2="722"/>
    <text class="label" x="230" y="748" font-size="18" text-anchor="middle">Date</text>
  </svg>
</main>
</body>
</html>
```